Eyecatcher-Broschüre für Hochzeitsfotografen
Perfekte und sehr angenehme Zusammenarbeit, bei der das optimale Ergebnis im Fokus stand. Super Einsatz - vielen Dank dafür!
Zielgruppe
Hochzeitsfotograf aus Köln / fotografiert deutschlandweit exklusive Hochzeitsreportagen
Zielgruppe: moderne Paare, designorientiert, offen, fotobegeistert mit dem Blick für das besondere Foto, welches die Geschichte ihres Hochzeitstages erzählt. Paare, die einen Künstler suchen und keinen Dienstleister !
Aufgabenstellung
Format DIN A5 oder DIN A4 - zwei erste Entwurfseiten füge ich als PDF bei, so dass man schon eine Idee erhält, wie ich es mir vorstellen kann. Ich bin aber offen für Neues.
Weniger ist Mehr!
puristische Gestaltung ohne viele Schnörkel - aber zeitgemäß und aktuell - Broschüre sollte maximal 8 Seiten haben - Lust auf mehr sollte durch eine aussergewöhnliche Broschüre entstehen.
Bild & Textmaterial kann für den Entwurf von meiner Webseite verwendet werden: jorisklaff-brautbilder.de

```html
<!DOCTYPE html>
<html lang="de">
<head>
<meta charset="utf-8">
<title>Broschüre – Hochzeitsfotografie</title>
<link href="https://fonts.googleapis.com/css2?family=Playfair+Display:wght@700;900&family=Raleway:wght@400;500;600&display=swap" rel="stylesheet">
<style>
  :root{
    --backdrop:#ece6e2;
    --paper:#d4d5d1;
    --paper-shade:#c6c7c3;
    --ink-light:#ffffff;
    --ink-muted:#8a8a86;
    --ink-caption:#55565a;
    --accent:#c7aaa2;
    --wall:#f3f2f0;
    --suit:#8d9197;
    --tie:#d63f86;
    --dress:#ece8e6;
    --frame:#ffffff;
  }
  *{margin:0;padding:0;box-sizing:border-box}
  html,body{width:1200px;height:814px;overflow:hidden;background:var(--backdrop)}

  .spread{
    position:absolute;left:180px;top:87px;width:840px;height:640px;
    display:flex;box-shadow:0 18px 40px rgba(80,60,50,.18);
  }
  .page{position:relative;width:420px;height:640px;background:var(--paper);overflow:hidden}
  .page--left{background:linear-gradient(90deg,var(--paper) 88%,var(--paper-shade))}
  .page--right{background:linear-gradient(90deg,var(--paper-shade),var(--paper) 10%)}

  .intro{position:absolute;left:46px;top:118px;width:270px;color:var(--ink-light);
    text-shadow:0 0 2px rgba(90,90,85,.35)}
  .intro__title{font-family:"Playfair Display",serif;font-weight:900;font-size:26px;line-height:1.1;letter-spacing:.2px}
  .intro__rule{width:26px;height:2px;background:var(--ink-light);margin:12px 0 12px}
  .intro__text{font-family:"Raleway",sans-serif;font-weight:600;font-size:12px;line-height:1.45;margin-bottom:15px}

  .url{position:absolute;left:46px;bottom:40px;font-family:"Raleway",sans-serif;font-weight:500;font-size:12.5px;color:var(--ink-muted);letter-spacing:.3px}

  .brand{position:absolute;display:flex;align-items:center;gap:7px;font-family:"Raleway",sans-serif;font-weight:500;font-size:10px;color:var(--accent);letter-spacing:.3px}
  .brand__dot{width:26px;height:26px;border-radius:50%;background:var(--accent);opacity:.75}
  .page--left .brand{right:34px;bottom:40px}
  .page--right .brand{left:40px;bottom:40px}

  .photo{position:absolute;left:118px;top:0;width:302px;height:640px;
    background:
      radial-gradient(ellipse 40% 30% at 72% 78%, rgba(214,63,134,.28), transparent 70%),
      linear-gradient(180deg,var(--wall) 0%,var(--wall) 30%,var(--dress) 55%,var(--suit) 100%);}
  .photo__frame{position:absolute;left:36px;top:78px;width:346px;height:300px;border:1.5px solid var(--frame)}
  .photo__caption{position:absolute;right:26px;top:200px;writing-mode:vertical-rl;
    font-family:"Raleway",sans-serif;font-weight:500;font-size:11px;color:var(--ink-caption);letter-spacing:.4px}
</style>
</head>
<body>
  <main class="spread">
    <section class="page page--left">
      <div class="intro">
        <h1 class="intro__title">stilvoll, emotional<br>&amp; einzigartig</h1>
        <div class="intro__rule"></div>
        <p class="intro__text">Wenn Ihr mich für Eure Hochzeit als Fotograf bucht, erhaltet Ihr einen Freund für den Tag:</p>
        <p class="intro__text">Der mitdenkt, Euch als Ruhepol zur Seite steht, sich als Künstler und Gast perfekt in die Hochzeitsgesellschaft integriert und — das Wichtigste — einfach für Euch da ist.</p>
        <p class="intro__text">Jedes Brautpaar und jede Feier ist einzigartig. Deshalb freue ich mich darauf, Euch persönlich kennenzulernen.</p>
        <p class="intro__text">Euer Joris</p>
      </div>
      <p class="url">www.jorisklaff-brautbilder.de</p>
      <div class="brand"><span class="brand__dot"></span></div>
    </section>

    <section class="page page--right">
      <div class="photo" role="img" aria-label="Fotografie eines lachenden Brautpaars vor heller Wand, Bräutigam im grauen Karoanzug mit pinker Krawatte, Braut im weißen Spitzenkleid mit rosa Blumenstrauß"></div>
      <div class="photo__frame"></div>
      <p class="photo__caption">Joris Klaff · Wedding Photography</p>
      <div class="brand"><span class="brand__dot"></span></div>
    </section>
  </main>
</body>
</html>
```